Kettlelanternpress: Self-help book needs Promotional Postcard

Need a postcard 8.5" x 5.5" to promote my upcoming book. Its a self-help career book for women focusing on how the mother-daughter relationship impacts careers and tips and solutions for success. The model includes 5 different types of daughters.
Title: Where Did the Quiet Garden Lead Us?
Breathe new life into your career by understanding your mother daughter relationship.
Book release is January 9, 2017
Updates

I just uploaded 5 images of the daughter types without the words, better to use these, thanks! Added Thursday, December 29, 2016

Target Market(s)

This book is targeted towards women

Industry/Entity Type

Promotional

Font styles to use
Serif
Other font styles liked:
• see website text

Colors
00a990
ec252d
e34297

Requirements
Must have
• Eye catching promotional postcard. Must have image of book on front with title and subtitle, author name and website. I'd like images of the 5 daughters on the front.
• Colors should match the cover green and pink
• Back can have quotes and author bio
• can look at website (not quite completed) for more inspiration www.kettlelanternpress.example
Nice to have
• Curious to see how the postcard compliments the book and website.

```html
<!DOCTYPE html>
<html lang="en">
<head>
<meta charset="utf-8">
<title>Where Did the Quiet Garden Lead Us? – Postcard</title>
<link href="https://fonts.googleapis.com/css2?family=Arimo:ital,wght@0,400;0,700;1,700&family=Gelasio:ital@1&display=swap" rel="stylesheet">
<style>
  :root {
    --frame-green: #0f5a52;
    --berry: #ad0f55;
    --berry-soft: #c41f69;
    --ink: #2c2a2b;
    --white: #ffffff;
    --cover-olive: #8e9c66;
    --hair-pink: #f2b8d0;
  }
  * { box-sizing: border-box; margin: 0; padding: 0; }
  html, body { width: 1200px; height: 400px; overflow: hidden; background: var(--white); }
  body { position: relative; font-family: "Arimo", Arial, sans-serif; }

  .card {
    position: absolute; top: 5px; height: 388px;
    background: var(--frame-green);
  }
  .card--front { left: 6px; width: 586px; }
  .card--back { left: 606px; width: 588px; }

  .title-panel {
    position: absolute; left: 22px; top: 20px; width: 542px; height: 118px;
    background: var(--berry); color: var(--white); text-align: center;
    padding-top: 12px;
  }
  .title-panel__title {
    font-weight: 700; font-size: 26px; line-height: 27px; letter-spacing: 2px;
  }
  .title-panel__subtitle {
    margin-top: 12px; font-weight: 700; font-size: 14.5px; line-height: 15px; letter-spacing: 1.2px;
  }

  .feature-panel {
    position: absolute; left: 22px; top: 158px; width: 542px; height: 197px;
    background: var(--berry);
  }
  .feature-panel__figure {
    position: absolute; left: 22px; top: 0; width: 132px; height: 197px;
    background: linear-gradient(90deg, var(--white) 0%, var(--white) 45%, var(--hair-pink) 75%, var(--berry) 100%);
  }
  .feature-panel__quote {
    position: absolute; left: 158px; top: 36px; width: 250px;
    font-family: "Gelasio", Georgia, serif; font-style: italic;
    color: var(--white); font-size: 14px; line-height: 20px; white-space: nowrap;
  }
  .feature-panel__attribution {
    display: block; margin-top: 10px; padding-left: 76px; font-size: 15.5px;
  }
  .feature-panel__book {
    position: absolute; right: 0; top: 0; width: 128px; height: 197px;
    background: linear-gradient(180deg, #97a56e 0%, var(--cover-olive) 100%);
  }

  .site-url {
    position: absolute; left: 0; width: 100%; top: 356px; text-align: center;
    color: #dfe9e6; font-weight: 700; font-style: italic; font-size: 18px; letter-spacing: 3.5px;
  }

  .back-panel {
    position: absolute; left: 20px; top: 20px; width: 548px; height: 342px;
    background: radial-gradient(ellipse at 50% 45%, #d4407e 0%, var(--berry-soft) 60%, #b3165d 100%);
    color: var(--ink); text-align: center;
  }
  .endorsement {
    position: absolute; left: 30px; right: 30px; top: 18px;
    font-weight: 700; font-size: 16.5px; line-height: 18px; letter-spacing: 1.3px;
  }
  .endorsement__source {
    display: block; margin-top: 4px; font-size: 12px; line-height: 14px; letter-spacing: 0.6px;
  }
  .author-bio {
    position: absolute; left: 30px; right: 30px; top: 205px;
    font-size: 12.5px; line-height: 14px; letter-spacing: 0.9px;
  }
</style>
</head>
<body>
  <section class="card card--front">
    <header class="title-panel">
      <h1 class="title-panel__title">Where Did the Quiet Garden<br>Lead Us?</h1>
      <p class="title-panel__subtitle">Breathe new life into your career by understanding<br>your mother daughter relationship.</p>
    </header>
    <div class="feature-panel">
      <div class="feature-panel__figure" role="img" aria-label="Illustration of a woman in profile silhouette with long pink hair"></div>
      <p class="feature-panel__quote">“Sometimes I feel like an imposter”<span class="feature-panel__attribution">-Dragonfly Dana</span></p>
      <div class="feature-panel__book" role="img" aria-label="Book cover of Where Did the Quiet Garden Lead Us? by Renata Solberg Hale, M.A., M.Ed"></div>
    </div>
    <p class="site-url">www.kettlelanternpress.example</p>
  </section>

  <section class="card card--back">
    <div class="back-panel">
      <blockquote class="endorsement">
        “...Renata draws the reader in with her poignant and insightful perspective of how family dynamics, particularly the conscious and subconscious aspects of the mother/daughter relationship, impact a career path and a fulfilled life...”
        <cite class="endorsement__source">Judge Marianne Colletti, COURT CORNER,<br>a syndicated TV court program.</cite>
      </blockquote>
      <p class="author-bio">Renata Solberg Hale, M.A., M.Ed. is a clinical career counselor and licensed mental health counselor who has been helping clients make meaningful career transitions and address workplace challenges for over 26 years. She is the 2013 recipient of the Outstanding Career Practitioner Award from the Regional Career Guidance Council. ‘Quiet Garden’ integrates her expertise in career development with her training and insight about the adult mother-daughter relationship.</p>
    </div>
  </section>
</body>
</html>
```